CLS Business card, letterhead, and stationery, email tag, fax cover
Clear and Professional material
Simple
Léandre Ormessac
Directeur des ventes
47, rue de Valmorin
Paris , 75016
France
leandre@clsys.fr
www.clsys.fr
Logo + tag line
LOGO
SMALL LOGO

```html
<!DOCTYPE html>
<html lang="fr">
<head>
<meta charset="utf-8">
<title>CLS – Cartes de visite</title>
<link href="https://fonts.googleapis.com/css2?family=Open+Sans:wght@400;600;700&family=Tinos&display=swap" rel="stylesheet">
<style>
  :root {
    --page-bg: #e9e7e4;
    --card-bg: #ffffff;
    --brand-blue: #3fb6d9;
    --brand-blue-light: #8fd6ea;
    --ink: #3c3c3c;
    --ink-soft: #6a6a6a;
    --rule: #9a9a9a;
    --band-grey: #7c7f83;
  }
  * { box-sizing: border-box; margin: 0; padding: 0; }
  html, body { width: 1200px; height: 852px; overflow: hidden; }
  body {
    background: var(--page-bg);
    position: relative;
    font-family: "Tinos", "Times New Roman", serif;
    color: var(--ink);
  }
  .card {
    position: absolute;
    width: 560px;
    height: 330px;
    background: var(--card-bg);
    border-radius: 18px;
    overflow: hidden;
    box-shadow: 0 4px 14px rgba(0,0,0,.18);
  }
  .card--front { left: 70px; top: 70px; }
  .card--back  { left: 570px; top: 452px; }

  .band { position: absolute; left: 0; bottom: 0; width: 560px; height: 110px; }

  .logo { position: absolute; text-align: center; }
  .logo__name {
    font-family: "Open Sans", Arial, sans-serif;
    font-weight: 600;
    color: var(--brand-blue);
    font-size: 20px;
    line-height: 1.1;
    display: flex; align-items: center; justify-content: center; gap: 8px;
  }
  .logo__mark {
    width: 14px; height: 14px; border-radius: 50%;
    background: var(--brand-blue); flex: none;
  }
  .logo__tagline {
    font-family: "Open Sans", Arial, sans-serif;
    font-size: 11px;
    color: var(--brand-blue);
    margin-top: 6px;
  }

  .divider { position: absolute; width: 1px; background: var(--rule); }

  .person__name {
    font-family: "Open Sans", Arial, sans-serif;
    font-weight: 700;
    color: var(--brand-blue);
    font-size: 15px;
  }
  .person__role { font-size: 13px; color: var(--ink); margin-top: 2px; }
  .address { font-size: 13.5px; line-height: 1.3; margin-top: 12px; }

  .contacts { list-style: none; position: absolute; font-size: 13.5px; }
  .contacts li { display: flex; align-items: center; gap: 8px; height: 19px; }
  .contacts svg { width: 12px; height: 12px; flex: none; }

  /* front */
  .card--front .logo { left: 20px; top: 108px; width: 240px; }
  .card--front .divider { left: 270px; top: 18px; height: 230px; }
  .card--front .person { position: absolute; left: 286px; top: 20px; }
  .card--front .contacts { left: 286px; top: 150px; }

  /* back */
  .card--back .logo { left: 230px; top: 42px; width: 310px; }
  .card--back .divider { left: 235px; top: 120px; height: 118px; }
  .card--back .person { position: absolute; left: 30px; top: 138px; width: 190px; text-align: center; }
  .card--back .address { text-align: right; }
  .card--back .contacts { left: 252px; top: 128px; }
</style>
</head>
<body>

<svg width="0" height="0" style="position:absolute" aria-hidden="true">
  <defs>
    <symbol id="icon-phone" viewBox="0 0 12 12"><path d="M3 1 L5 3.5 L4 5 Q5 7 7 8 L8.5 7 L11 9 L9.5 11 Q4 10.5 1 3 Z" fill="#3fb6d9"/></symbol>
    <symbol id="icon-mobile" viewBox="0 0 12 12"><rect x="3" y="0.5" width="6" height="11" rx="1.2" fill="#3fb6d9"/><rect x="4" y="2" width="4" height="7" fill="#fff"/></symbol>
    <symbol id="icon-fax" viewBox="0 0 12 12"><rect x="1" y="4" width="10" height="6" rx="1" fill="#3fb6d9"/><rect x="3" y="1" width="6" height="4" fill="#8fd6ea"/></symbol>
    <symbol id="icon-mail" viewBox="0 0 12 12"><circle cx="6" cy="6" r="5.5" fill="#3fb6d9"/><circle cx="6" cy="6" r="2" fill="none" stroke="#fff" stroke-width="1.2"/></symbol>
    <symbol id="icon-web" viewBox="0 0 12 12"><circle cx="6" cy="6" r="5.5" fill="#3fb6d9"/><path d="M0.5 6 H11.5 M6 0.5 V11.5" stroke="#fff" stroke-width=".8"/><ellipse cx="6" cy="6" rx="2.4" ry="5.5" fill="none" stroke="#fff" stroke-width=".8"/></symbol>
  </defs>
</svg>

<!-- Front card -->
<section class="card card--front">
  <div class="logo">
    <div class="logo__name"><span class="logo__mark"></span>Corvane Lumis Systems</div>
    <div class="logo__tagline">solutions avancées de la peau</div>
  </div>
  <div class="divider"></div>
  <div class="person">
    <div class="person__name">Léandre Ormessac</div>
    <div class="person__role">Directeur des ventes</div>
    <div class="address">47, rue de Valmorin<br>Paris , 75016<br>France</div>
  </div>
  <ul class="contacts">
    <li><svg><use href="#icon-phone"/></svg>01.40.72.15.36</li>
    <li><svg><use href="#icon-mobile"/></svg>06.18.44.70.25</li>
    <li><svg><use href="#icon-fax"/></svg>01.40.72.15.37</li>
    <li><svg><use href="#icon-mail"/></svg>leandre@clsys.fr</li>
    <li><svg><use href="#icon-web"/></svg>www.clsys.fr</li>
  </ul>
  <svg class="band" viewBox="0 0 560 110" preserveAspectRatio="none" aria-hidden="true">
    <path d="M0 72 Q260 60 560 8 L560 22 Q260 72 0 82 Z" fill="var(--band-grey)"/>
    <path d="M0 86 Q270 76 560 26 L560 110 L0 110 Z" fill="var(--brand-blue)"/>
    <path d="M0 96 Q280 86 560 46 L560 110 L0 110 Z" fill="var(--brand-blue-light)" opacity=".45"/>
  </svg>
</section>

<!-- Back card -->
<section class="card card--back">
  <div class="logo">
    <div class="logo__name"><span class="logo__mark"></span>Corvane Lumis Systems</div>
    <div class="logo__tagline">solutions avancées de la peau</div>
  </div>
  <div class="divider"></div>
  <div class="person">
    <div class="person__name">Léandre Ormessac</div>
    <div class="person__role">Directeur des ventes</div>
    <div class="address">47, rue de Valmorin<br>Paris , 75016<br>France</div>
  </div>
  <ul class="contacts">
    <li><svg><use href="#icon-phone"/></svg>01.40.72.15.36</li>
    <li><svg><use href="#icon-mobile"/></svg>06.18.44.70.25</li>
    <li><svg><use href="#icon-fax"/></svg>01.40.72.15.37</li>
    <li><svg><use href="#icon-mail"/></svg>leandre@clsys.fr</li>
    <li><svg><use href="#icon-web"/></svg>www.clsys.fr</li>
  </ul>
  <svg class="band" viewBox="0 0 560 110" preserveAspectRatio="none" aria-hidden="true">
    <path d="M0 40 Q300 92 560 66 L560 72 Q300 98 0 48 Z" fill="var(--band-grey)"/>
    <path d="M0 54 Q300 102 560 78 L560 110 L0 110 Z" fill="var(--brand-blue)"/>
    <path d="M0 76 Q300 110 560 94 L560 110 L0 110 Z" fill="var(--brand-blue-light)" opacity=".5"/>
  </svg>
</section>

</body>
</html>
```